Business card design needed

A small accounting firm that has relocated from the regional areas of Australia, to be city based, and using the resources of The Cloud to remake and streamline its operations, and wanting to share the benefits with small businesses all over Australia. We provide services on a fixed price basis, and run regular events for clients and potential clients.

Major product partners are Quorel Ledgering, Gatherloom, SlotFinch, Tallo and Pagemoss.

Please review the update to the brief.

Thanks.

Reason: Just swamped by good designs, need more time to provide feedback and make choices. Thanks in advance for the great efforts so far!

Need cards for 2 people

1. Dennis Halvorsen, Development Director
Mobile - 0499 572 438
dennis@fernbrookledger.example

2. Ruth Okonedo, Accountant
Mobile - 0488 164 729
ruth@fernbrookledger.example

Please check the amendments to the brief regarding web address etc.

Reason: Wanting some revisions before final selection.

Target Market(s)

Micro and Small business owners, trades, service and hospitality industries. Web savvy.

Industry/Entity Type

Accounting

Contact Information for Business Card

Fernbrook Ledger,
Level 5, Harwick Lane Plaza,
127 Harwick Lane, Melbourne, 3000

Logo Text

Fernbrook Ledger - Ledger Accounting and Business Solutions

Logo styles of interest
Abstract Logo
Requirements
Must have
• Must include some tagline for our services - eg Accounting & Business services, Fixed Price, Tax

On Reverse side
Twitter Address - @FernbrookLedgerAu
Facebook - www.socialpage.example/FernbrookLedger
Book Online Appointment (Slot Finch) - www.shortlink.example/ledgerslot
Nice to have
• The Quorel Logo - We are a Quorel Partner. Guidelines for logo use have been uploaded.

```html
<!DOCTYPE html>
<html lang="en">
<head>
<meta charset="utf-8">
<title>Fernbrook Ledger – Business Card</title>
<link rel="stylesheet" href="https://fonts.googleapis.com/css2?family=Roboto+Condensed:wght@300;500&display=swap">
<style>
  :root {
    --sky: #7ddffc;
    --brand-blue: #33c9ef;
    --ink: #333333;
    --paper-light: #f6f7f8;
    --paper-shade: #e2e5e7;
    --white: #ffffff;
  }
  * { margin: 0; padding: 0; box-sizing: border-box; }
  html, body { width: 1200px; height: 693px; overflow: hidden; background: var(--white); }
  .card {
    position: relative;
    width: 1200px;
    height: 693px;
    overflow: hidden;
    font-family: "Roboto Condensed", "Arial Narrow", sans-serif;
    color: var(--ink);
  }
  .card__backdrop {
    position: absolute;
    inset: 0;
    background: radial-gradient(circle at 60% 40%, var(--paper-light), var(--paper-shade));
  }
  .card__cloud {
    position: absolute;
    inset: 0;
    width: 1200px;
    height: 693px;
  }
  .brand {
    position: absolute;
    left: 780px;
    top: 92px;
    color: var(--brand-blue);
    font-weight: 500;
    font-size: 58px;
    line-height: 1.05;
    letter-spacing: 1px;
    text-transform: uppercase;
  }
  .tagline {
    position: absolute;
    left: 94px;
    top: 312px;
    font-weight: 300;
    font-size: 32px;
    line-height: 45px;
  }
  .divider {
    position: absolute;
    left: 0;
    top: 439px;
    width: 728px;
    border-top: 2px dashed var(--white);
  }
  .address {
    position: absolute;
    left: 94px;
    top: 471px;
    font-style: normal;
    font-weight: 500;
    font-size: 33px;
    line-height: 48px;
  }
</style>
</head>
<body>
  <main class="card">
    <div class="card__backdrop" role="img" aria-label="Soft background of scattered white three-dimensional numerals"></div>

    <svg class="card__cloud" viewBox="0 0 1063 614" aria-hidden="true">
      <path fill="var(--sky)" d="M0,172 C30,168 42,150 62,138 C112,112 205,118 252,160 C298,128 382,140 420,190 C485,182 560,232 582,300 C642,332 672,420 650,480 C672,530 662,580 642,614 L0,614 Z"/>
    </svg>

    <h1 class="brand">Fernbrook<br>Ledger</h1>

    <p class="tagline">Accounting solutions<br>for small businesses</p>

    <div class="divider"></div>

    <address class="address">
      FERNBROOK LEDGER<br>
      Level 5, Harwick Lane Plaza<br>
      127 Harwick Lane, Melbourne VIC 3000
    </address>
  </main>
</body>
</html>
```